Letterhead for financial advisor-insurance agent firm

Our company, Marlowe Thistle Insurance & Investments, is an insurance (health, life, home, auto, etc) and investment brokerage offering a suite of options to meet client needs. We need letterhead that is professional and embodies strength, security and sophistication.

Industry/Entity Type

Investment

```html
<!DOCTYPE html>
<html lang="en">
<head>
<meta charset="utf-8">
<title>Marlowe Thistle Insurance &amp; Investments — Letterhead</title>
<link rel="stylesheet" href="https://fonts.googleapis.com/css2?family=Cinzel:wght@400;600&family=Cardo&family=Open+Sans:wght@400&display=swap">
<style>
  :root {
    --navy: #2b3157;
    --navy-text: #242a4f;
    --band-text: #e8eaf2;
    --icon: #7d8aa0;
    --paper: #ffffff;
    --backdrop: #ecedf0;
  }
  * { box-sizing: border-box; margin: 0; padding: 0; }
  html, body { width: 1200px; height: 1048px; overflow: hidden; }
  body {
    background: var(--backdrop);
    display: flex;
    align-items: center;
    justify-content: center;
  }
  .letterhead {
    position: relative;
    width: 760px;
    height: 984px;
    background: var(--paper);
    box-shadow: 0 4px 18px rgba(30, 34, 60, 0.18);
  }
  .header-band {
    position: absolute;
    top: 56px;
    left: 148px;
    right: 0;
    height: 46px;
    background: var(--navy);
    display: flex;
    align-items: center;
    padding-left: 54px;
    gap: 44px;
    color: var(--band-text);
  }
  .header-band .web {
    font-family: "Cardo", serif;
    font-size: 17px;
    letter-spacing: 1.5px;
  }
  .header-band .email {
    display: flex;
    align-items: center;
    gap: 10px;
    font-family: "Open Sans", sans-serif;
    font-size: 15px;
  }
  .brand {
    position: absolute;
    top: 48px;
    left: 46px;
  }
  .brand-mark {
    width: 44px;
    height: 44px;
    margin-left: 62px;
    border: 2px solid var(--navy);
    background: var(--paper);
  }
  .brand-name {
    margin-top: 8px;
    font-family: "Cinzel", serif;
    font-weight: 400;
    font-size: 23px;
    line-height: 1;
    color: var(--navy-text);
  }
  .brand-tagline {
    margin-top: 3px;
    margin-left: 34px;
    font-family: "Cinzel", serif;
    font-size: 9px;
    letter-spacing: 0.6px;
    color: var(--navy-text);
  }
  .footer-band {
    position: absolute;
    left: 0;
    right: 0;
    bottom: 0;
    height: 88px;
    background: var(--navy);
    display: flex;
    align-items: center;
    padding: 0 40px;
    font-family: "Open Sans", sans-serif;
    font-size: 12px;
    color: var(--band-text);
  }
  .contact-item {
    display: flex;
    align-items: center;
    gap: 10px;
  }
  .contact-item.address { flex: 1; }
  .contact-item.phone { margin-left: 70px; }
  .icon { fill: var(--icon); flex: none; }
</style>
</head>
<body>
  <main class="letterhead">
    <header>
      <div class="header-band">
        <span class="web">www.marlowethistle.com</span>
        <span class="email">
          <svg class="icon" width="24" height="18" viewBox="0 0 24 18" aria-hidden="true">
            <rect x="1" y="1" width="22" height="16" rx="2" fill="none" stroke="#7d8aa0" stroke-width="2"/>
            <path d="M2 3 L12 10 L22 3" fill="none" stroke="#7d8aa0" stroke-width="2"/>
          </svg>
          info@marlowethistle.com
        </span>
      </div>
      <div class="brand">
        <div class="brand-mark"></div>
        <div class="brand-name">Marlowe Thistle</div>
        <div class="brand-tagline">Insurance &amp; Investments</div>
      </div>
    </header>

    <footer class="footer-band">
      <span class="contact-item address">
        <svg class="icon" width="20" height="18" viewBox="0 0 20 18" aria-hidden="true">
          <path d="M10 1 L19 9 H16 V17 H12 V12 H8 V17 H4 V9 H1 Z"/>
        </svg>
        Marlowe Thistle Building, 2715 N. Harbor Ave, Ste.
      </span>
      <span class="contact-item phone">
        <svg class="icon" width="20" height="16" viewBox="0 0 20 16" aria-hidden="true">
          <path d="M1 6 C1 2 19 2 19 6 L19 8 L14 8 L14 5.5 C12 5 8 5 6 5.5 L6 8 L1 8 Z"/>
          <path d="M4 9 H16 L18 15 H2 Z"/>
        </svg>
        (555) 218-3046
      </span>
      <span class="contact-item phone">
        <svg class="icon" width="20" height="16" viewBox="0 0 20 16" aria-hidden="true">
          <path d="M1 6 C1 2 19 2 19 6 L19 8 L14 8 L14 5.5 C12 5 8 5 6 5.5 L6 8 L1 8 Z"/>
          <path d="M4 9 H16 L18 15 H2 Z"/>
        </svg>
        (555) 218-3046
      </span>
    </footer>
  </main>
</body>
</html>
```